Concept design for a tea business Labels

Hello, we are looking for concepts for our label/packaging for a tea business that has been in business now for over a year. We are a beachy, organic, "It's your moment. Enjoy it." type tea business. We have an online website (www.corvalbrewhouse.com.au) and sell at local markets around the Tarrowby Cove area.
We are looking to upgrade our label to look more professional, in a fun/beachy/chilled out style. (unlike the traditional tea labels).
We do loose leaf tea and iced tea consentrated syrups. We have a few different packages (please see website under "sizes and packaging" bottom left). We would like to experiement with various different size and shape of labels for different products, so would like a concept design for a label using our logo (see website front page bottom). There are no colour constraints.
We use the Quillan brand labels of the following sizes:
1. Pure Glass Rectangular Product Labels, Q4825, 100/Pack, 96 x 50.8 mm
2. Pure Glass Round Multi-purpose Labels, Q3907D, 240/Pack, 40 mm diameter
3.Pure Glass Square Product Labels, Q4861, 350/Pack, 35 x 35 mm
4. For bottles we use Grained Ivory Curved Labels, Q4839, 90/Pack, 57.2 x 77 mm
If you have any more questions, please don't hesitate to contact me
Updates
Hi All,
I am considering using a box like below for packing and doing a bit of a white/beachy feel to the packaging. Either using the rectangle or round circle labels. (circle labels from quillan 60mm diameter).

Reason: Hi All - Thank you so much for all your designs. While I have seen some really beautiful designs I am excited about, it seems there was a rush at the end with a number of new designs just submitted. I still haven't seen just one design I love for the label, so I would like the opportunity to work with some of the new designers to see if we can modify to suit the concept.
Would anyone like to try a concept label with a silhouette of one of the following wave/beach/teacup? I'm just exploring a different approach as I know it is difficult tying in the beach with tea - please think - chilled out beach hut with tea/iced tea, sunrise over ocean. I like the soft colour palette - beachy feel to it - ie. Pastels - blues, greens, whites, sandy, pinks, purples, greys - sunrises over ocean, maybe a white rustic wood feel - or any other icon from Tarrowby Cove - like the Norfolk Pine's along the beach - maybe in Silhouette.
Just some more ideas.
Thank you again for all your contributions!
Petra

```html
<!DOCTYPE html>
<html lang="en">
<head>
<meta charset="utf-8">
<title>Tarrowby Tea Company – Round Labels</title>
<link rel="stylesheet" href="https://fonts.googleapis.com/css2?family=Noticia+Text:wght@400;700&family=Yanone+Kaffeesatz:wght@300;400&display=swap">
<style>
  :root {
    --lotus-green: #a8f350;
    --earl-pink: #ff5c80;
    --chamomile-yellow: #ffda6c;
    --ink: #50566a;
    --rim: #8d8d9c;
    --paper: #ffffff;
  }
  html, body {
    margin: 0;
    width: 1200px;
    height: 900px;
    overflow: hidden;
    background: var(--paper);
  }
  .label-sheet { display: block; width: 1200px; height: 900px; }
  .label-rim { fill: var(--paper); stroke: var(--rim); stroke-width: 1.2; }
  .brand-dot { fill: var(--paper); }
  .brand-name {
    font-family: "Yanone Kaffeesatz", sans-serif;
    font-weight: 300;
    font-size: 19px;
    fill: var(--paper);
    text-anchor: middle;
  }
  .tea-name {
    font-family: "Yanone Kaffeesatz", sans-serif;
    font-weight: 300;
    font-size: 40px;
    text-anchor: middle;
  }
  .ingredients {
    font-family: "Noticia Text", serif;
    font-size: 12.5px;
    fill: var(--ink);
    text-anchor: middle;
  }
  .ingredients .lead { font-weight: 700; }
  .web-address {
    font-family: "Noticia Text", serif;
    font-weight: 700;
    font-size: 14px;
    letter-spacing: 1px;
    fill: var(--ink);
  }
  .label--small .brand-name { font-size: 20px; }
  .label--small .tea-name { font-size: 37px; }
  .label--small .ingredients { font-size: 14.5px; }
  .label--small .web-address { font-weight: 400; font-size: 14px; letter-spacing: 0.5px; }
  .label--small .label-rim { stroke-width: 1.6; }

  .tint--green .band, .tint--green .tea-name { fill: var(--lotus-green); }
  .tint--pink .band, .tint--pink .tea-name { fill: var(--earl-pink); }
  .tint--yellow .band, .tint--yellow .tea-name { fill: var(--chamomile-yellow); }
</style>
</head>
<body>
<svg class="label-sheet" viewBox="0 0 1200 900" xmlns="http://www.w3.org/2000/svg">
  <defs>
    <clipPath id="label-face"><circle r="170"/></clipPath>
    <path id="web-arc-large" d="M -148 0 A 148 148 0 0 0 148 0"/>
    <path id="web-arc-small" d="M -140 0 A 140 140 0 0 0 140 0"/>
    <path id="wave-band" d="M -170 -180 H 180 V -42 q -8.5 -7 -17 0 t -17 0 t -17 0 t -17 0 t -17 0 t -17 0 t -17 0 t -17 0 t -17 0 t -17 0 t -17 0 t -17 0 t -17 0 t -17 0 t -17 0 t -17 0 t -17 0 t -17 0 t -17 0 t -17 0 t -17 0 V -180 Z"/>
  </defs>

  <!-- Large labels -->
  <g class="label tint--green" transform="translate(228 280)">
    <circle class="label-rim" r="170"/>
    <use class="band" href="#wave-band" clip-path="url(#label-face)"/>
    <circle class="brand-dot" cy="-120" r="36"/>
    <text class="brand-name" y="-55">TARROWBY TEA COMPANY</text>
    <text class="tea-name" y="36">Vietnamese Lotus Tea</text>
    <text class="ingredients" y="72"><tspan class="lead">Ingredients:</tspan> Vietnamese green tea and</text>
    <text class="ingredients" y="87">lotus leaves.</text>
    <text class="web-address"><textPath href="#web-arc-large" startOffset="50%" text-anchor="middle">www.corvalbrewhouse.com.au</textPath></text>
  </g>

  <g class="label tint--pink" transform="translate(599 280)">
    <circle class="label-rim" r="170"/>
    <use class="band" href="#wave-band" clip-path="url(#label-face)"/>
    <circle class="brand-dot" cy="-120" r="36"/>
    <text class="brand-name" y="-55">TARROWBY TEA COMPANY</text>
    <text class="tea-name" y="36">French Earl Grey</text>
    <text class="ingredients" y="72"><tspan class="lead">Ingredients:</tspan> Black tea, beromont oil, peach</text>
    <text class="ingredients" y="87">and rose petal.</text>
    <text class="web-address"><textPath href="#web-arc-large" startOffset="50%" text-anchor="middle">www.corvalbrewhouse.com.au</textPath></text>
  </g>

  <g class="label tint--yellow" transform="translate(972 280)">
    <circle class="label-rim" r="170"/>
    <use class="band" href="#wave-band" clip-path="url(#label-face)"/>
    <circle class="brand-dot" cy="-120" r="36"/>
    <text class="brand-name" y="-55">TARROWBY TEA COMPANY</text>
    <text class="tea-name" y="36">Chamomile Blue Moon</text>
    <text class="ingredients" y="72"><tspan class="lead">Ingredients:</tspan> Chamomile flowers,</text>
    <text class="ingredients" y="87">peppermint blue, cornflowers, and</text>
    <text class="ingredients" y="102">pomegranate flowers.</text>
    <text class="web-address"><textPath href="#web-arc-large" startOffset="50%" text-anchor="middle">www.corvalbrewhouse.com.au</textPath></text>
  </g>

  <!-- Small labels -->
  <g class="label label--small tint--green" transform="translate(228 676) scale(0.665)">
    <circle class="label-rim" r="170"/>
    <use class="band" href="#wave-band" clip-path="url(#label-face)"/>
    <circle class="brand-dot" cy="-114" r="37"/>
    <text class="brand-name" y="-50">TARROWBY TEA COMPANY</text>
    <text class="tea-name" y="32">Vietnamese Lotus Tea</text>
    <text class="ingredients" y="62"><tspan class="lead">Ingredients:</tspan> Vietnamese green tea</text>
    <text class="ingredients" y="79">and lotus leaves.</text>
    <text class="web-address"><textPath href="#web-arc-small" startOffset="50%" text-anchor="middle">www.corvalbrewhouse.com.au</textPath></text>
  </g>

  <g class="label label--small tint--pink" transform="translate(599 676) scale(0.665)">
    <circle class="label-rim" r="170"/>
    <use class="band" href="#wave-band" clip-path="url(#label-face)"/>
    <circle class="brand-dot" cy="-114" r="37"/>
    <text class="brand-name" y="-50">TARROWBY TEA COMPANY</text>
    <text class="tea-name" y="32">French Earl Grey</text>
    <text class="ingredients" y="62"><tspan class="lead">Ingredients:</tspan> Black tea, beromont oil,</text>
    <text class="ingredients" y="79">peach and rose petal.</text>
    <text class="web-address"><textPath href="#web-arc-small" startOffset="50%" text-anchor="middle">www.corvalbrewhouse.com.au</textPath></text>
  </g>

  <g class="label label--small tint--yellow" transform="translate(972 676) scale(0.665)">
    <circle class="label-rim" r="170"/>
    <use class="band" href="#wave-band" clip-path="url(#label-face)"/>
    <circle class="brand-dot" cy="-114" r="37"/>
    <text class="brand-name" y="-50">TARROWBY TEA COMPANY</text>
    <text class="tea-name" y="32">Chamomile Blue Moon</text>
    <text class="ingredients" y="62"><tspan class="lead">Ingredients:</tspan> Chamomile flowers,</text>
    <text class="ingredients" y="79">peppermint blue, cornflowers,</text>
    <text class="ingredients" y="96">and pomegranate flowers.</text>
    <text class="web-address"><textPath href="#web-arc-small" startOffset="50%" text-anchor="middle">www.corvalbrewhouse.com.au</textPath></text>
  </g>
</svg>
</body>
</html>
```